Innovative Consulting Firm Needs New Business Cards and Stationary

Our Innovative Consulting Firm, Larkfield Consulting, is in need of new business cards and stationary designs. We want two-sided cards that incorporate our logo, which is attached. We are looking for something not too formal, but is professional and slick.

Card should have the following information:
Name (ex. Tom Bradley)
Title (ex. Manager)
Address (ex. 24680 Cedar Lane)
Address 2 (ex. Suite 100)
City
State
Zip Code
Mobile
Email

The card should also have our website: www.larkfieldconsulting.example

Industry/Entity Type

Management Consulting

Contact Information for Business Card

Name (ex. Tom Bradley)
Title (ex. Manager)
Address 2 (ex. Suite 100)
City
State
Zip Code
Mobile
Email

Font styles to use
Sans Serif

Requirements
Must have
• The colors on the card must match the colors in the logo. The exact color codes are attached in a pdf.
Nice to have
• The Company's Tagline is "Focused on your Future". This might be nice to incorporate, but not necessary.

```html
<!DOCTYPE html>
<html lang="en">
<head>
<meta charset="utf-8">
<title>Larkfield Consulting – Business Cards</title>
<link rel="stylesheet" href="https://fonts.googleapis.com/css2?family=Montserrat:wght@400;500;600&family=Noto+Serif:wght@400;700&display=swap">
<style>
  :root {
    --navy: #1d3f72;
    --navy-deep: #0f2a55;
    --steel: #3a6ea5;
    --amber: #f0a01e;
    --ink: #2b2b2b;
    --muted: #9a9a9a;
    --paper: #ffffff;
    --backdrop: #ecebe8;
  }
  * { box-sizing: border-box; margin: 0; padding: 0; }
  html, body { width: 1200px; height: 913px; overflow: hidden; }
  body {
    background: var(--backdrop);
    font-family: "Montserrat", sans-serif;
    display: flex;
    align-items: center;
    justify-content: center;
    gap: 40px;
  }
  .card {
    position: relative;
    width: 540px;
    height: 309px;
    background: var(--paper);
    box-shadow: 0 2px 10px rgba(0,0,0,0.12);
    overflow: hidden;
  }
  /* Front */
  .card-front .wordmark {
    position: absolute;
    left: 0; right: 0;
    top: 100px;
    display: flex;
    align-items: center;
    justify-content: center;
    gap: 12px;
    white-space: nowrap;
  }
  .wordmark-dot {
    width: 18px; height: 18px;
    border-radius: 50%;
    background: var(--amber);
    flex: none;
  }
  .wordmark-name {
    font-weight: 500;
    font-size: 36px;
    color: var(--navy);
    line-height: 1;
  }
  .tagline {
    position: absolute;
    left: 0; right: 0;
    top: 210px;
    text-align: center;
    font-size: 14px;
    font-weight: 500;
    letter-spacing: 9px;
    color: var(--navy);
    white-space: nowrap;
  }
  .tagline .accent { color: var(--amber); font-weight: 600; }

  /* Back */
  .card-back .sweep { position: absolute; inset: 0; }
  .card-back .wordmark-light {
    position: absolute;
    left: 34px;
    top: 206px;
    font-weight: 500;
    font-size: 22px;
    color: var(--paper);
    white-space: nowrap;
  }
  .contact {
    position: absolute;
    left: 312px;
    top: 28px;
    font-family: "Noto Serif", serif;
    color: var(--ink);
  }
  .contact-name { font-size: 22px; line-height: 1.1; white-space: nowrap; }
  .contact-name .surname { color: var(--steel); font-weight: 700; }
  .contact-title { font-size: 13px; color: var(--muted); margin-bottom: 12px; }
  .contact-list { list-style: none; font-size: 9.5px; line-height: 1.5; white-space: nowrap; }
  .contact-list li { display: flex; align-items: flex-start; gap: 6px; }
  .contact-list li.gap { margin-top: 6px; }
  .contact-list svg { flex: none; margin-top: 2px; }
</style>
</head>
<body>

  <section class="card card-front" aria-label="Card front">
    <div class="wordmark">
      <span class="wordmark-dot"></span>
      <span class="wordmark-name">Larkfield Consulting</span>
    </div>
    <p class="tagline">FOCUSED ON <span class="accent">YOUR</span> FUTURE</p>
  </section>

  <section class="card card-back" aria-label="Card back">
    <svg class="sweep" width="540" height="309" viewBox="0 0 540 309" aria-hidden="true">
      <defs>
        <linearGradient id="deepBlue" x1="0" y1="0" x2="0" y2="1">
          <stop offset="0" stop-color="#2a5a94"/>
          <stop offset="1" stop-color="#0f2a55"/>
        </linearGradient>
      </defs>
      <path d="M0,0 H200 C210,140 320,230 540,262 V309 H0 Z" fill="#3a6ea5"/>
      <path d="M186,0 C196,150 310,240 540,275" fill="none" stroke="#ffffff" stroke-width="5"/>
      <path d="M0,0 H170 C180,160 300,252 540,290 V309 H0 Z" fill="url(#deepBlue)"/>
    </svg>

    <div class="wordmark-light">Larkfield Consulting</div>

    <div class="contact">
      <p class="contact-name">Tom <span class="surname">BRADLEY</span></p>
      <p class="contact-title">Manager</p>
      <ul class="contact-list">
        <li>
          <svg width="10" height="10" viewBox="0 0 10 10" aria-hidden="true"><circle cx="5" cy="5" r="5" fill="var(--navy)"/><rect x="2.5" y="3.3" width="5" height="3.4" fill="none" stroke="#fff" stroke-width="0.8"/><path d="M2.5,3.3 L5,5.3 L7.5,3.3" fill="none" stroke="#fff" stroke-width="0.8"/></svg>
          tom.bradley@larkfieldconsulting.example
        </li>
        <li>
          <svg width="10" height="10" viewBox="0 0 10 10" aria-hidden="true"><circle cx="5" cy="5" r="5" fill="var(--navy)"/><path d="M3.3,2.6 C3,4.6 5,6.9 7.2,6.8 L7.2,6 L6,5.5 L5.5,6 C4.6,5.6 4.2,5.1 3.9,4.4 L4.4,3.9 L3.9,2.6 Z" fill="#fff"/></svg>
          555-014-2837
        </li>
        <li>
          <svg width="10" height="10" viewBox="0 0 10 10" aria-hidden="true"><circle cx="5" cy="5" r="5" fill="var(--navy)"/><circle cx="5" cy="5" r="2.8" fill="none" stroke="#fff" stroke-width="0.7"/><path d="M2.2,5 H7.8 M5,2.2 C3.6,3.8 3.6,6.2 5,7.8 C6.4,6.2 6.4,3.8 5,2.2" fill="none" stroke="#fff" stroke-width="0.6"/></svg>
          www.larkfieldconsulting.example
        </li>
        <li class="gap">
          <svg width="10" height="10" viewBox="0 0 10 10" aria-hidden="true"><circle cx="5" cy="5" r="5" fill="var(--navy)"/><path d="M2.4,5.2 L5,2.8 L7.6,5.2 M3.3,4.6 V7.2 H6.7 V4.6" fill="none" stroke="#fff" stroke-width="0.8"/></svg>
          <span>24680 Cedar Lane, Suite 100<br>80512 Fairview, CA</span>
        </li>
      </ul>
    </div>
  </section>

</body>
</html>
```